Oil and Gas Industry training School Needs a Web Design

We need a web design for a new company based in Northern British Columbia Canada called "SKILLPATH Trade Academy Inc." Is a training facility that specializes in different aspects of Pipeline Construction training. We also offer compliance courses for Oil and Gas Industry. We would like to see designs that us the colours in our logo.

Target Market(s)

Is Men and women between 18-60 that want to work in the oil and gas industry

Industry/Entity Type

School

Number of Pages Required

5+ page

Font styles to use
Sans Serif

Colors
f37022
000000
333333
ffffff
848484
7f7f7f
c8c8c8
f68d4d
fee3d4

Requirements
Must have
• a easy back end for editing content! and adding additional pages if necessary.

```html
<!DOCTYPE html>
<html lang="en">
<head>
<meta charset="utf-8">
<title>SKILLPATH Trade Academy Inc.</title>
<link rel="stylesheet" href="https://fonts.googleapis.com/css2?family=Jost:wght@400;500;600&family=Merriweather:wght@400;700&display=swap">
<style>
:root{
  --orange:#f37022;
  --orange-soft:#f68d4d;
  --black:#000000;
  --charcoal:#333333;
  --white:#ffffff;
  --grey:#848484;
  --grey-light:#c8c8c8;
  --peach:#fee3d4;
  --sans:'Jost',sans-serif;
  --serif:'Merriweather',serif;
}
*{box-sizing:border-box;margin:0;padding:0}
html,body{width:853px;height:1200px;overflow:hidden;background:var(--white)}
body{position:relative;font-family:var(--sans);color:var(--charcoal)}
.hero{position:absolute;left:0;top:0;width:853px;height:508px;
  background:linear-gradient(180deg,#6b4a45 0%,#9a6a55 14%,#5a5a6a 30%,#2f4f78 46%,#3f6f9e 58%,#274a62 70%,#1c2f2a 86%,#13201c 100%)}
.site-header{position:absolute;left:0;top:0;width:853px;height:50px;background:rgba(0,0,0,.72)}
.brand{position:absolute;left:26px;top:0;height:50px;display:flex;align-items:center;gap:8px;color:var(--white);font-weight:600;font-size:12px;line-height:13px;letter-spacing:.4px}
.brand-dot{flex:none;width:22px;height:22px;border-radius:50%;background:var(--orange)}
.main-nav{position:absolute;left:0;top:0;height:50px;width:720px}
.main-nav a{position:absolute;top:0;color:var(--white);text-decoration:none;font-size:14px;height:50px;line-height:50px;white-space:nowrap}
.main-nav a:nth-child(1){left:231px}
.main-nav a:nth-child(2){left:338px}
.main-nav a:nth-child(3){left:424px}
.main-nav a:nth-child(4){left:530px}
.main-nav a:nth-child(5){left:658px}
.main-nav a.active{color:var(--orange)}
.main-nav a.active::after{content:"";position:absolute;left:-6px;right:-6px;bottom:0;height:2px;background:var(--orange)}
.weather{position:absolute;right:0;top:0;width:118px;height:50px;border-left:1px solid #444;text-align:center;color:var(--orange)}
.weather small{display:block;font-size:9.5px;margin-top:6px}
.weather strong{display:block;font-size:18px;font-weight:500;margin-top:2px}
.hero-title{position:absolute;left:0;width:853px;top:190px;text-align:center;color:var(--white);font-size:37px;line-height:48px;font-weight:400}
.hero-title em{font-style:normal;color:var(--orange)}
.btn-outline{position:absolute;left:350px;top:310px;width:175px;height:30px;border:1.5px solid var(--white);color:var(--white);font-size:15px;text-align:center;line-height:27px}
.ticker{position:absolute;left:0;top:461px;width:853px;height:47px;background:rgba(10,14,14,.75);display:flex;align-items:center}
.ticker-item{color:var(--orange);font-size:14.5px;display:flex;align-items:center;gap:14px;white-space:nowrap}
.ticker-item:first-child{margin-left:18px;padding-right:18px;border-right:1px solid #555}
.ticker-item:last-child{margin-left:46px}
.intro{position:absolute;left:0;top:508px;width:521px;height:135px;background:var(--orange);color:var(--white);padding:17px 22px}
.intro p{font-family:var(--serif);font-size:12.2px;line-height:20px}
.intro p b{font-weight:700}
.link-arrow{display:flex;align-items:center;gap:14px;font-size:13px;letter-spacing:.5px;text-transform:uppercase;white-space:nowrap}
.intro .link-arrow{margin-top:14px}
.intro-photo{position:absolute;left:521px;top:508px;width:332px;height:135px;background:linear-gradient(180deg,#7a8f9c 0%,#a8b4b0 35%,#5b6a48 60%,#3c4a2e 100%)}
.about{position:absolute;left:0;top:643px;width:853px;height:213px;text-align:center;padding:14px 170px 0}
.about p{font-family:var(--serif);font-size:11.5px;line-height:21px;color:var(--charcoal);margin-bottom:12px}
.about p b{color:var(--orange);font-weight:700}
.about .link-arrow{justify-content:center;color:var(--charcoal);margin-top:4px}
.profile-photo{position:absolute;left:0;top:856px;width:341px;height:208px;background:linear-gradient(135deg,#6d6a5e 0%,#9c9a8c 40%,#2f8a4c 70%,#3b4a3f 100%)}
.profile{position:absolute;left:341px;top:856px;width:512px;height:208px;background:var(--orange);color:var(--white);padding:22px 30px 0 32px}
.profile h2{font-weight:400;font-size:30px;line-height:36px;white-space:nowrap}
.profile p{font-family:var(--serif);font-size:11.4px;line-height:20px;margin-top:16px}
.profile .link-arrow{margin-top:16px}
.site-footer{position:absolute;left:0;top:1064px;width:853px;height:136px;background:var(--black);color:var(--white)}
.footer-brand{position:absolute;left:72px;top:46px;display:flex;align-items:center;gap:8px;font-weight:600;font-size:12px;line-height:13px;letter-spacing:.4px}
.footer-col{position:absolute;top:20px}
.footer-col h3{font-size:12px;font-weight:500;letter-spacing:.5px;margin-bottom:5px;white-space:nowrap}
.footer-col p{font-family:var(--serif);font-size:6.3px;line-height:9px}
.col-about{left:302px;width:102px}
.col-contact{left:432px;width:90px}
.col-connect{left:559px;width:140px}
.social{display:flex;gap:8px;margin-top:7px}
.social span{width:10px;height:10px;border-radius:50%;background:var(--white)}
.copyright{position:absolute;left:0;width:853px;bottom:8px;text-align:center;font-size:6.5px;letter-spacing:1px}
</style>
</head>
<body>
<section class="hero">
  <div role="img" aria-label="Photograph of a mountain lake in Northern British Columbia with forested shores at dusk" style="position:absolute;inset:0"></div>
  <header class="site-header">
    <div class="brand"><span class="brand-dot"></span><span>SKILLPATH<br>Trade Academy Inc.</span></div>
    <nav class="main-nav">
      <a href="#">training</a>
      <a href="#">staffing</a>
      <a href="#">compliance</a>
      <a href="#" class="active">pipeline safety</a>
      <a href="#">contact</a>
    </nav>
    <div class="weather"><small>today in Prince George</small><strong>58°/36°</strong></div>
  </header>
  <h1 class="hero-title">our job is to help <em>you</em><br>prepare for <em>your</em> job.</h1>
  <div class="btn-outline">learn more</div>
  <div class="ticker">
    <div class="ticker-item">Few places remaining for November Pipeline Safety Course
      <svg width="8" height="16" viewBox="0 0 8 16"><path d="M1 1l6 7-6 7" fill="none" stroke="#f37022" stroke-width="1.6"/></svg></div>
    <div class="ticker-item">New office to open in December in Vanderhoof
      <svg width="8" height="16" viewBox="0 0 8 16"><path d="M1 1l6 7-6 7" fill="none" stroke="#f37022" stroke-width="1.6"/></svg></div>
  </div>
</section>

<section class="intro">
  <p>Northern British Columbia is home to one of the world's fastest growing oil and gas industries. At <b>skillpath</b>, we help make British Columbia's workforce ready to meet the demand for jobs these industries will create.</p>
  <div class="link-arrow"><svg width="8" height="16" viewBox="0 0 8 16"><path d="M1 1l6 7-6 7" fill="none" stroke="#fff" stroke-width="1.6"/></svg>Learn more about what we do</div>
</section>
<div class="intro-photo" role="img" aria-label="Photograph of a large pipeline running through a forest with mountains behind"></div>

<section class="about">
  <p><b>skillpath trade academy</b> works hand in hand with some of Canada's largest oil and gas suppliers in order to provide them with hard-working and well trained employees. With the ever growing demand in the energy industry, these companies are looking for workers to contribute both in and out of the field. We play the largest role in preparing them.</p>
  <p>like you, <b>we're from Prince George</b>, so we know how <b>talented</b> and <b>driven</b> this community is. By preparing our friends and family for better and more challenging jobs, we are paving the way for the best and brightest future our wonderful town can have.</p>
  <div class="link-arrow"><svg width="8" height="16" viewBox="0 0 8 16"><path d="M1 1l6 7-6 7" fill="none" stroke="#333" stroke-width="1.6"/></svg>Learn more</div>
</section>

<div class="profile-photo" role="img" aria-label="Photograph of a graduate in a hard hat and green rain gear standing among industrial pipes"></div>
<section class="profile">
  <h2>graduate profile: marcus hale</h2>
  <p>Vanderhoof resident Marcus Hale took our Pipeline Safety course last spring, and found a job less than one week after completion. Since then, he's traveled all around Canada working for Northline Energy. He tells us his story.</p>
  <div class="link-arrow"><svg width="8" height="16" viewBox="0 0 8 16"><path d="M1 1l6 7-6 7" fill="none" stroke="#fff" stroke-width="1.6"/></svg>Read Marcus's story</div>
</section>

<footer class="site-footer">
  <div class="footer-brand"><span class="brand-dot"></span><span>SKILLPATH<br>Trade Academy Inc.</span></div>
  <div class="footer-col col-about"><h3>ABOUT</h3><p>skillpath is a training facility specializing in different aspects of Pipeline Construction training. We also offer compliance courses for Oil and Gas Industry.</p></div>
  <div class="footer-col col-contact"><h3>CONTACT</h3><p>1180 Ridgeway Avenue<br>Prince George, BC<br>Canada V2K 4R7<br><br>info@skillpathtrade.ca<br>(250) 555-0148</p></div>
  <div class="footer-col col-connect"><h3>CONNECT AND FOLLOW</h3><p>Every day we publish new offers and training availabilities, as well as recent job developments, on our social channels. Be sure to follow us to stay up to date!</p>
    <div class="social" aria-label="Social links"><span></span><span></span></div></div>
  <div class="copyright">COPYRIGHT 2014</div>
</footer>
</body>
</html>
```